依頼詳細
概要、特徴にも書いたように、今回、分離発注に向けた営業用のチラシを作成して頂きたいです。

・すでに既存で新規顧客獲得用のパンフレット(高難度松浦工業)とチラシ(HARUKAZE)があり、今回は、それらに追加で挟む “分離発注を目的としたチラシ” の依頼となります。

※既存(高難度パンフレット)(添付資料1、2)
+
既存(HARUKAZE)(添付資料3)
+
“分離発注を目的としたチラシ”

既存の3つのチラシ(※添付資料1.2.3)と一緒に挟んで、配布したいので

流れを理解して作成していただけたら幸いです。

・流れ、
株式会社松浦工業は、高難度の足場を専門で営業しています。

また、その職人で構成されている、HARUKAZEというワンランク上の足場サービスも運営しています。(住人さんや近隣様、などへの配慮、最高のサービスを提供するブランド)
(HARUKAZEにもホームページがございます。)

安全には、費用がかかります。
人の命は尊いです。
工事は足場から始まり、足場で終わります。
そして、業者みんなが使う足場です。

弊社の売りを武器として運営し維持して行くためには、無駄な予算を削り、その予算を安心できる工事に生かす。

そして見た目も美しい職人で揃えている私たちと手を組みませんか。

。。。といった流れでイメージして作成して頂きたいです。

※弊社の売りに関しましては、添付した資料やホームページを確認して頂き、理解して頂きたいです。

・目的は、新規顧客の獲得ですが、分離発注の提案を載せたいです。

・新規顧客(ターゲット)→ビル建物のオーナー、元請業社、ゼネコンなど

・メリットとデメリットをまとめたマインドマップも添付しますので、必要であれば使ってください。
・他にも、ホームページもありますので、見ていただけたら、と思います。
・弊社は改修工事用の足場をメインで運営しております。
(居住者様や、近隣様、歩行者様からの安心や業者間、現場管理監督様とのコミュニケーションもとても大切にしております。)
・メリットのマインドマップの他にも、弊社を使うことでのメリットは、たくさんあります。
・どの立場から見ても美しい足場屋を目指しております。

記載項目
分離発注しませんか。

株式会社松浦工業
042−718−2964
https://matsuurakogyo-ashiba.example
↑↑
株式会社松浦工業(高難度専門の足場サービス)

https://harukaze-ashiba.example
↑↑
ワンランク上の足場サービス
HARUKAZE ホームページ

サイズ
A4
ページ数
両面
希望イメージ
シンプル 複雑
単色 カラフル
暗い 明るい
日常 高級
遊び心 厳粛
未来的 伝統的
女性的 男性的
希望する色
黄・オレンジ系、緑系、青系、既存チラシ(添付資料1.2.3)とのバランスで決めて頂きたい
納品ファイル
• 高解像度JPG (.jpg)
• イラストレーター形式 (.ai)
補足説明
↑↑
株式会社松浦工業(高難度専門の足場サービス)

↑↑
ワンランク上の足場サービス
HARUKAZE ホームページ

どちらも並行して運営しております!

ーーーーーーーーーーーーーーーーーーーーーーーーー

※多少の文字の変更などがしやすいように、アウトライン化されていないデータでも納品して頂きたいです。
みなさま、すばらしい作品をありがとうございます!

みなさまの作品を見て間違えに気づくことが出来ました。

一部、変更させてください!

3点あるのですが、

①1つ目は、このチラシを誰に当てた手紙にするのか、ですが、ターゲットは、
・ビルやマンション、学校など建物のオーナー様
・ビルやマンションの管理をしている管理会社様や、
・不動産会社様
・店舗、等の工事担当者様
に当てた手紙で作成して頂きたいです。

※よく考えたら工事会社が直接足場屋に依頼するのは、当前のことだと思いましたので、工事業者に当てるのはおかしい話だと気付いたので宜しくお願いいたします。

②見積もり依頼までの流れを盛り込んで頂きたいです。
流れ
平日の9:00〜17:00に
042−718−2964

に電話をして頂き、弊社の電話に出た物に、見積もりして欲しい物件のご住所をお聞かせください。

or

当社ホームページ問い合わせフォームのQRコード?
かURL??

で見積もり依頼のメッセージを頂けたら、

1週間以内にTerravue Mapsを元に概算でお見積もりして郵送させて頂きます。

※建物の改修工事が決まりましたら、弊社と工事業者様とで直接お打ち合わせして、施工します!
※安心、安全へのクオリティは、高品質をお約束しますので、安心してください。
※足場工事は、命の危険を伴う工事です。

。。。のような感じをうまく刺さる形で表現して頂きたいです。

③ターゲットに分離発注という意味を理解してもらえるのかも不安になってきたのですが、どうでしょうか。

このチラシに足場だけを分離発注しませんか?なのか、
直接発注しませんか、なのか、何か良い表現があればそれも考えていただけると幸いです。

分離発注でわかるから大丈夫だよ、であれば分離発注も構いません。
ただ僕が不安になっただけなので、
そこも何か良い案があればなーと思ったので、宜しくお願いいたします。

コロナで、大ダメージを受けてしまったので、これで、復活したいと考えております!

みなさま、どうか宜しくお願いいたします!

弊社の既存のパンフレットと一緒に配ることを踏まえてこの作品が一番良いのではないかと感じました。

この度は、本当にありがとうございました。
僕たちは、職人さん達の生活がもっと潤っていけるように、したいと考えております。
職人さん達の世界では土曜も仕事をすることが当たり前となっております。
しかし僕たちは価値の高い仕事を社会に広めていき、みんなが、より良い工事をしながら、生活も潤っていけるように考えております。
皆さんが作ってくれた作品から、僕たちは大きな気づきをゲットしました!
とても感謝しています。
本当に本当にありがとうございました。

```html
<!DOCTYPE html>
<html lang="ja">
<head>
<meta charset="UTF-8">
<title>分離発注のご案内 | 株式会社松浦工業</title>
<link rel="stylesheet" href="https://fonts.googleapis.com/css2?family=Noto+Serif+JP:wght@400;600;700;900&display=swap">
<style>
  :root {
    --navy: #1d2b4c;
    --navy-soft: #3a4a6b;
    --ink: #1f2430;
    --paper: #ffffff;
    --rule: #9aa3b5;
    --photo-a: #5f6f86;
    --photo-b: #2f3d55;
  }
  * { margin: 0; padding: 0; box-sizing: border-box; }
  html, body { width: 846px; height: 1200px; overflow: hidden; background: var(--paper); }
  body { font-family: "Noto Serif JP", serif; color: var(--ink); }
  .flyer { position: relative; width: 846px; height: 1200px; background: var(--paper); }

  .photo {
    position: absolute;
    background: linear-gradient(135deg, var(--photo-a) 0%, var(--photo-b) 100%);
  }
  .photo--crew { left: 268px; top: 22px; width: 352px; height: 226px; }
  .photo--safety { left: 28px; top: 418px; width: 352px; height: 232px; }
  .photo--team { left: 255px; top: 735px; width: 380px; height: 225px; }

  .section-label {
    position: absolute;
    background: var(--navy);
    color: var(--paper);
    font-weight: 900;
    font-size: 26px;
    letter-spacing: 0.04em;
    padding: 4px 12px;
    line-height: 1.15;
  }
  .section-sub {
    position: absolute;
    font-size: 11px;
    color: var(--navy-soft);
  }
  .section-num {
    position: absolute;
    font-size: 64px;
    font-weight: 900;
    color: var(--navy);
    line-height: 1;
    letter-spacing: 0.02em;
  }
  .section-num::after {
    content: "";
    display: block;
    width: 100%;
    height: 3px;
    background: var(--navy);
    margin-top: 6px;
  }
  .body-copy {
    position: absolute;
    font-size: 14px;
    line-height: 1.75;
    color: var(--ink);
    text-align: justify;
  }

  .about-label { left: 30px; top: 40px; }
  .about-sub { left: 34px; top: 86px; }
  .about-num { left: 30px; top: 150px; }
  .about-copy { left: 30px; top: 258px; width: 570px; }

  .site-link {
    position: absolute;
    left: 185px; top: 356px; width: 420px;
    border: 1px solid var(--rule);
    text-align: center;
    padding: 6px 10px;
  }
  .site-link__caption { font-size: 11px; color: var(--navy-soft); }
  .site-link__url { font-size: 13px; font-weight: 600; color: var(--navy); margin-top: 2px; }

  .safety-label { left: 405px; top: 430px; font-size: 30px; padding: 6px 14px; }
  .safety-sub { left: 410px; top: 508px; }
  .safety-num { left: 405px; top: 550px; }
  .safety-copy { left: 30px; top: 662px; width: 590px; }

  .order-label { left: 30px; top: 742px; font-size: 24px; padding: 6px 12px; }
  .order-sub { left: 34px; top: 820px; }
  .order-num { left: 30px; top: 870px; }
  .order-copy { left: 30px; top: 972px; width: 600px; font-size: 13.5px; line-height: 1.7; }

  .tagline {
    position: absolute;
    writing-mode: vertical-rl;
    color: var(--navy);
    font-weight: 900;
    white-space: nowrap;
  }
  .tagline--lead { right: 18px; top: 20px; font-size: 58px; letter-spacing: 0.1em; }
  .tagline--sub { right: 112px; top: 24px; font-size: 42px; letter-spacing: 0.06em; }

  .footer {
    position: absolute;
    left: 30px; right: 30px; top: 1120px;
    border-top: 1px solid var(--rule);
    text-align: center;
    padding-top: 8px;
  }
  .footer__note { font-size: 13px; color: var(--ink); }
  .footer__company {
    font-size: 32px; font-weight: 900; color: var(--navy);
    letter-spacing: 0.08em; margin-top: 4px;
  }
</style>
</head>
<body>
<main class="flyer">

  <div class="photo photo--crew" role="img" aria-label="足場の上で作業する職人たちの写真"></div>
  <h2 class="section-label about-label">ABOUT US</h2>
  <p class="section-sub about-sub">私たちについて</p>
  <div class="section-num about-num">01.</div>
  <p class="body-copy about-copy">株式会社松浦工業は、高難度の改修工事の足場をメインに、足場専門で営業しています。また、その職人で構成されているHARUKAZEというワンランク上の足場サービスも運営しています。「HARUKAZE」は住人さんや近隣様、などへの配慮、そして最高のサービスを提供するブランドです。</p>
  <div class="site-link">
    <p class="site-link__caption">ワンランク上の足場サービス HARUKAZE ホームページ</p>
    <p class="site-link__url">https://harukaze-ashiba.example</p>
  </div>

  <div class="photo photo--safety" role="img" aria-label="ヘルメットを着用した職人の写真"></div>
  <h2 class="section-label safety-label">SAFETY<br>FIRST</h2>
  <p class="section-sub safety-sub">安全第一</p>
  <div class="section-num safety-num">02.</div>
  <p class="body-copy safety-copy">安全には、費用がかかります。人の命は尊いです。工事は足場から始まり、足場で終わります。そして、業者みんなが使う足場です。私たちは、どの立場から見ても機能的で美しい足場屋を目指しています。</p>

  <h2 class="section-label order-label">DIRECT<br>ORDER</h2>
  <p class="section-sub order-sub">分離発注</p>
  <div class="section-num order-num">03.</div>
  <div class="photo photo--team" role="img" aria-label="現場に並ぶ足場職人チームの写真"></div>
  <p class="body-copy order-copy">私たちは居住者様や、近隣様、歩行者様からの安心や業者間、現場管理監督様とのコミュニケーションもとても大切にしています。弊社の売りを武器として運営し維持して行くためには、無駄な予算を削り、その予算を安心できる工事に生かす。そして見た目も美しい職人で揃えている私たちと手を組みませんか。ご期待以上の仕事をお約束いたします。</p>

  <h1 class="tagline tagline--lead">命を守る、工事現場の要。</h1>
  <p class="tagline tagline--sub">足場専門の松浦工業で、ワンランク上の足場サービスを。</p>

  <footer class="footer">
    <p class="footer__note">分離発注について、詳しくは裏面でご紹介しております。</p>
    <p class="footer__company">株式会社松浦工業</p>
  </footer>

</main>
</body>
</html>
```